wedding / conference Banner Ad Design Project

We require 4 banner ads for the one company. Each one is for a slightly different theme so may have different images, layout, wording etc. We are understanding that the area provided is very small but would like the ability to use images either in each banner, or as the background of each banner.

Business is www.lanternbrookestate.com.au

The 4 banners will be for the following, Weddings, Conference, Retreats (with the 4th being another wedding banner with slightly different text).

They must all have the same Font, and similar style or feel preferred, fit in aesthetically with our own website and meet the following criteria. We have also noted preferences for particular concepts and Ideas but we use pixel forum to see other peoples ideas and concepts so please don't be afraid to offer ideas or other designs that you might think good options. We will list ideas for each different type of banner at the bottom here.

We have also uploaded a rough idea of what we were thinking here, by no means is it meant to dictate design, just give you a good mental picture of what we originally had in mind.

1. Similar font and "feel" preferred for each banner.

2. 728 x 90 Pixels (requirement) (HORIZONTAL BANNER PLEASE, we have uploaded a file called banner example that is a very rough concept to give you ideas)

3. File size under 130 kb (requirement)

4. Logo from Webpage to be copied and used or the least the wavey mountain "frame and feel" We have attached a previous banner to explain this concept please feel free to use the idea in different ways.

5. Would prefer to see a couple of different ideas for "background" here. This is not essential but would like to see banners that are white, black (similar to our webpage) and possibly using photos instead to take advantage of our view etc.

6. Any design must look good on any kind of background as it may be used on any number of sites.

7. Must say "The Lantern Brook Estate" and "Blue Mountains" on every banner. Must also have somewhere our catchphrase "So close by ... but worlds away" but this can be smaller and only as an inclusion to make everything the same across the board.

Now for the individual banners as follows some ideas and requirements.

Wedding : - Must have upmarket feel and we are picturing a white background (but open to ideas still, this might also be nice with a range of images as background somehow) Main text is "Blue Mountains Wedding Venue". Must say "exclusive use, ceremony, reception, and accommodation in a private, majestic location." and also if possible "Full weekend event weddings, tailored to your taste and budget". We also have many many wedding pictures on our own webpage in the wedding gallery. This one would be great to have images used in a clever way to show the beauty and flexibility of the venue. We can provide preferred images if needed but for now designers can grab them from the site to facilitate a large array of images to suit various ideas.

Wedding banner 2 : - can be very similar to the first but must say prominently "Weekend event wedding packages with 2 nights accommodation, ceremony, reception catering, beverages, equipment, setup & breakfasts from $290 pp."

Conference : - Conference banner can be more simple, must have upmarket feel, we are picturing a black background (but open to ideas still). Main text is "Blue Mountains Conference Venue" Must say "Personal, inspiring conference venue in a magnificent private location". Also would like it say somewhere "Flexible, tailored, accommodated events from 10 to 50 people".

Retreats : - Main text is "Blue Mountains Retreat" Must also say "Private, personal, quiet venue on 32 acres of virgin bushland in the heart of The Blue Mountains" and "Completely flexible, tailored packages, to help achieve the retreat your attendees are looking for". This one is to appeal to more "meditation, spiritual" kinds of retreats so we were thinking maybe lots of images of the view and surrounds etc. Again open to ideas and have no real plans for setup.

Target Market(s)

Wedding & Conferences (upmarket) Plus Retreats (meditation etc)

Industry/Entity Type

Accommodation

Requirements
Nice to have
• Upmarket feel, but still getting across the friendly relaxing atmosphere. Is that possible in an area that small!?!
Should not have
• No PINK!
Must not use images that are not from the business. No stolen images from the web and no images of random people taken from the web.

```html
<!DOCTYPE html>
<html lang="en">
<head>
<meta charset="utf-8">
<title>The Lantern Brook Estate – Banner Set</title>
<link rel="stylesheet" href="https://fonts.googleapis.com/css2?family=PT+Sans:wght@400;700&display=swap">
<style>
  :root {
    --page-bg: #262626;
    --frame: #f2f2f2;
    --brand-panel: #3b342d;
    --brand-ink: #e6f0d8;
    --night: #1c1e2c;
    --teal-head: #6cc6dc;
    --white: #ffffff;
    --leather: #a8703f;
    --leather-dark: #8a5a30;
    --gold-head: #f0d95c;
    --sky-top: #a9c6de;
    --sky-low: #f4f6f6;
    --navy-head: #1d5c8a;
    --ink: #2e2e2e;
    --strip: rgba(0, 0, 0, 0.55);
  }
  * { box-sizing: border-box; margin: 0; padding: 0; }
  html, body { width: 1200px; height: 768px; overflow: hidden; }
  body {
    background: var(--page-bg);
    font-family: "PT Sans", "Segoe UI", Arial, sans-serif;
    position: relative;
  }
  .banner {
    position: absolute;
    left: 66px;
    width: 1049px;
    height: 130px;
    border: 1px solid var(--frame);
    overflow: hidden;
  }
  .banner--wedding { top: 66px; background: var(--night); }
  .banner--weekend { top: 229px; background: var(--night); }
  .banner--conference { top: 393px; background: linear-gradient(90deg, var(--leather-dark), var(--leather) 40%, var(--leather)); }
  .banner--retreat { top: 556px; background: linear-gradient(180deg, var(--sky-top), var(--sky-low) 85%); }

  .brand {
    position: absolute; left: 0; top: 0;
    width: 202px; height: 100%;
    background: var(--brand-panel);
    display: flex;
    align-items: flex-end; justify-content: center;
    padding-bottom: 16px;
    text-align: center;
  }
  .brand__name {
    color: var(--brand-ink);
    font-size: 20px; font-weight: 400; line-height: 1.15;
    letter-spacing: 0.5px;
  }

  .photo {
    position: absolute; top: 0; right: 0; height: 100%;
  }
  .photo--table { width: 330px; background: linear-gradient(110deg, var(--night) 0%, #3a2f3a 25%, #4a4552 55%, #d9d9dc 90%); }
  .photo--fan { width: 330px; background: linear-gradient(110deg, var(--night) 0%, #5a2b35 30%, #b3384a 55%, #eaeaea 85%); }
  .photo--lodge { width: 330px; background: linear-gradient(100deg, var(--leather) 0%, #9a5a3e 30%, #6b5a50 60%, #3e4b3a 100%); }
  .photo--bush { width: 460px; background: linear-gradient(90deg, rgba(255,255,255,0) 0%, rgba(90,100,95,0.35) 45%, rgba(40,45,40,0.8) 100%); }

  .copy {
    position: absolute; left: 226px; top: 14px;
    width: 560px;
  }
  .copy__headline { font-size: 30px; font-weight: 700; line-height: 1.15; margin-bottom: 6px; }
  .copy__detail { font-size: 18px; font-weight: 700; line-height: 1.45; }
  .banner--wedding .copy__headline,
  .banner--weekend .copy__headline { color: var(--teal-head); }
  .banner--wedding .copy__detail,
  .banner--weekend .copy__detail,
  .banner--conference .copy__detail { color: var(--white); }
  .banner--conference .copy__headline { color: var(--gold-head); }
  .banner--retreat .copy__headline { color: var(--navy-head); }
  .banner--retreat .copy__detail { color: var(--ink); font-weight: 400; }

  .tagline {
    position: absolute; right: 0; bottom: 0;
    width: 282px; height: 30px;
    background: var(--strip);
    color: var(--white);
    font-size: 17px; line-height: 30px;
    text-align: center;
  }
</style>
</head>
<body>

<section class="banner banner--wedding">
  <div class="photo photo--table" role="img" aria-label="Photo of a dressed wedding reception table with glassware and rose petals"></div>
  <div class="brand"><span class="brand__name">The Lantern<br>Brook Estate</span></div>
  <div class="copy">
    <h2 class="copy__headline">Blue Mountains Wedding Venue</h2>
    <p class="copy__detail">exclusive use, ceremony, reception, and<br>accommodation in a private, majestic location</p>
  </div>
  <p class="tagline">So close by … but worlds away</p>
</section>

<section class="banner banner--weekend">
  <div class="photo photo--fan" role="img" aria-label="Photo of a red paper fan on a wedding table"></div>
  <div class="brand"><span class="brand__name">The Lantern<br>Brook Estate</span></div>
  <div class="copy">
    <h2 class="copy__headline">Blue Mountains Weekend Event</h2>
    <p class="copy__detail">wedding packgaes with 2 nights accommodation,<br>ceremony, beverages, &amp; more from $290 pp</p>
  </div>
  <p class="tagline">So close by … but worlds away</p>
</section>

<section class="banner banner--conference">
  <div class="photo photo--lodge" role="img" aria-label="Photo of the brick lodge building with gabled roofs"></div>
  <div class="brand"><span class="brand__name">The Lantern<br>Brook Estate</span></div>
  <div class="copy">
    <h2 class="copy__headline">Blue Mountains Conference Venue</h2>
    <p class="copy__detail">Personal, inspiring conference venue in a magnificent<br>private location from 10 to 50 people</p>
  </div>
  <p class="tagline">So close by … but worlds away</p>
</section>

<section class="banner banner--retreat">
  <div class="photo photo--bush" role="img" aria-label="Photo of gum tree branches against a pale sky"></div>
  <div class="brand"><span class="brand__name">The Lantern<br>Brook Estate</span></div>
  <div class="copy">
    <h2 class="copy__headline">Blue Mountains Retreat</h2>
    <p class="copy__detail">Private, personal, quiet venue on 32 acres of virgin<br>bushland in the heart of The Blue Mountains</p>
  </div>
  <p class="tagline">So close by … but worlds away</p>
</section>

</body>
</html>
```